Our company needs a Corporate Identity Package!!!

We would like to receive submissions for a corporate identity pachage including the following elements:

1. Presentation Folder
2. Product/Service Catalogue (16 A4 pages landscape but expandable)
3. Product Brochure (up to 8 A4 pages)
4. Product Flyer (2 A4 pages)
5. Business Card
6. Letterhead
7. Envelope
8. E-mail signature.

I attach a Presentation Folder that i like (geometric but also has circle). We would like to have some ideas regarding the above 7 elements including vantrime logo colors (vantrime.example).

Payment is indicative and we are planning to increase the payment now that we found out how to actually do this. You are also more than welcome to send us a message and suggest the amount of payment for your Corporate Identity elements and we will update this.

Target Market(s)

Home | Office | Life

Colors
f78f20
0555a3
9bcb3b

Requirements
Must have
• 1. Presentation Folder
• 2. Product/Service Catalogue (16 A4 pages landscape but to be easily expandable)
• 3. Product Brochure (up to 4 A4 pages but to be easily expandable )
• 4. Product Flyer (2 A4 pages)
• 5. Business Card
• 6. Letterhead
• 7. Envelope
• 8. E-mail signature.
Nice to have
• It would be nice to include design something around the cycle that communicates the best six doctors (i.e. sunshine, water, rest, air, exercise and diet) !!!

```html
<!DOCTYPE html>
<html lang="en">
<head>
<meta charset="utf-8">
<title>Vantrime — Corporate Identity Set</title>
<link href="https://fonts.googleapis.com/css2?family=Raleway:wght@400;500;600&family=Open+Sans:wght@400;600;700&display=swap" rel="stylesheet">
<style>
  :root{
    --board:#a293a8;
    --navy:#2b2f8f;
    --blue:#0555a3;
    --sky:#3fb5ea;
    --orange:#f78f20;
    --green:#5a9a3f;
    --lime:#9bcb3b;
    --paper:#ffffff;
    --mist:#eef0f2;
    --ink:#1d3f8f;
    --grey:#8a8f99;
  }
  *{box-sizing:border-box;margin:0;padding:0}
  html,body{width:1200px;height:1200px;overflow:hidden;background:var(--board)}
  .board{position:relative;width:1200px;height:1200px;font-family:"Open Sans",sans-serif}
  .piece{position:absolute;overflow:hidden;box-shadow:0 2px 6px rgba(0,0,0,.25)}
  .piece > svg{position:absolute;inset:0;width:100%;height:100%}
  .txt{position:absolute;white-space:nowrap}

  .brand{position:absolute;display:flex;align-items:center;gap:.35em}
  .brand-dot{width:1.15em;height:1.15em;border-radius:50%;background:var(--orange);flex:none}
  .brand-name{font-family:"Raleway",sans-serif;font-weight:500;color:var(--blue);line-height:1}
  .brand-tag{position:absolute;font-family:"Raleway",sans-serif;color:var(--grey);letter-spacing:.25em;white-space:nowrap}

  .tagline{font-family:"Raleway",sans-serif;color:#fff;font-weight:400}
  .url{font-family:"Raleway",sans-serif;color:#fff}

  .contact{display:flex;align-items:center;gap:3px;color:var(--ink);font-weight:600}
  .ico{width:1.1em;height:1.1em;flex:none}

  .folder-front{left:67px;top:48px;width:695px;height:490px;z-index:2}
  .folder-inside{left:438px;top:128px;width:698px;height:490px;z-index:1;background:var(--green)}
  .inside-sheet{position:absolute;left:381px;top:42px;width:296px;height:448px;background:var(--paper);box-shadow:0 1px 4px rgba(0,0,0,.25)}
  .sheet-body{position:absolute;left:24px;top:86px;width:256px;color:var(--ink);font-size:5.2px;line-height:1.85;font-weight:600}
  .sheet-body h3{font-size:6px;font-weight:700;margin-bottom:2px;color:#6aa52f}
  .sheet-body p{margin-bottom:8px}

  .letterhead{left:67px;top:598px;width:296px;height:408px;background:var(--paper)}
  .envelope-back{left:712px;top:669px;width:416px;height:214px;z-index:1}
  .envelope-front{left:469px;top:760px;width:425px;height:214px;background:var(--paper);z-index:2}
  .card{top:1046px;width:174px;height:104px;background:var(--paper);border-radius:6px}
  .card-front{left:70px}
  .card-back{left:254px}
</style>
</head>
<body>
<main class="board">

  <section class="piece folder-inside" aria-label="Presentation folder, inside">
    <svg viewBox="0 0 698 490" preserveAspectRatio="none">
      <defs>
        <linearGradient id="insideGlow" x1="0" y1="0" x2="1" y2="0">
          <stop offset="0" stop-color="#5e9e44"/><stop offset=".6" stop-color="#4e8c3a"/><stop offset="1" stop-color="#5a9a3f"/>
        </linearGradient>
      </defs>
      <rect role="img" aria-label="Faded photo of a woman exercising" width="698" height="490" fill="url(#insideGlow)"/>
    </svg>
    <div class="inside-sheet">
      <svg viewBox="0 0 296 448" style="position:absolute;inset:0;width:100%;height:100%">
        <rect x="0" y="6" width="150" height="4" fill="var(--orange)"/>
        <rect x="150" y="6" width="146" height="4" fill="var(--navy)"/>
        <line x1="24" y1="66" x2="284" y2="66" stroke="var(--orange)" stroke-width=".8"/>
      </svg>
      <div class="brand" style="left:16px;top:28px;font-size:17px"><span class="brand-dot"></span><span class="brand-name">vantrime</span></div>
      <div class="brand-tag" style="left:44px;top:46px;font-size:3.5px">HOME | OFFICE | LIFE</div>
      <div class="txt" style="left:196px;top:22px;font-size:5.6px;line-height:2.1">
        <div class="contact"><svg class="ico" viewBox="0 0 10 10"><circle cx="5" cy="5" r="4.3" fill="none" stroke="var(--orange)"/><path d="M3.4 3 l1 1-.5.6a3 3 0 0 0 1.5 1.5l.6-.5 1 1-.7.7C4.8 7.1 2.9 5.2 2.7 3.7z" fill="var(--orange)"/></svg>+1 555 0142 318</div>
        <div class="contact"><svg class="ico" viewBox="0 0 10 10"><circle cx="5" cy="5" r="4.3" fill="none" stroke="var(--orange)"/><rect x="2.8" y="3.5" width="4.4" height="3" fill="none" stroke="var(--orange)" stroke-width=".7"/></svg>manager@vantrime.example</div>
        <div class="contact"><svg class="ico" viewBox="0 0 10 10"><circle cx="5" cy="5" r="4.3" fill="none" stroke="var(--orange)"/><path d="M5 7.6 3.3 5A1.8 1.8 0 1 1 6.7 5z" fill="var(--orange)"/></svg>Physical, Address, Here</div>
      </div>
      <div class="sheet-body">
        <h3>BIT EATEMPERIAM QUAM EX ET,</h3>
        <p>Thank you for your interest in our home, office and life range. This letter outlines the products we discussed and the next steps for delivery and setup at your site.</p>
        <p>Our team will contact you within five working days to confirm the order and arrange a suitable time.</p>
        <p>Please keep this letter for your records and reach out with any questions at all.</p>
      </div>
    </div>
    <svg viewBox="0 0 698 490" preserveAspectRatio="none" style="z-index:3">
      <defs>
        <linearGradient id="pocketFill" x1="0" y1="0" x2="1" y2="0">
          <stop offset="0" stop-color="var(--navy)"/><stop offset="1" stop-color="var(--blue)"/>
        </linearGradient>
      </defs>
      <path d="M358 490 C370 430 380 412 430 405 L698 352 L698 490 Z" fill="url(#pocketFill)"/>
      <circle cx="705" cy="440" r="60" fill="#8f6d72" opacity=".75"/>
      <g transform="rotate(8 540 430)">
        <rect x="485" y="398" width="110" height="62" rx="4" fill="#fff"/>
        <polygon points="520,398 595,398 595,402 550,410" fill="var(--navy)"/>
        <rect x="485" y="452" width="110" height="5" fill="var(--navy)"/>
        <circle cx="506" cy="427" r="6" fill="var(--orange)"/>
        <text x="515" y="431" font-family="Raleway, sans-serif" font-size="12" font-weight="500" fill="var(--blue)">vantrime</text>
      </g>
    </svg>
  </section>

  <section class="piece folder-front" aria-label="Presentation folder, outside">
    <svg viewBox="0 0 695 490" preserveAspectRatio="none">
      <defs>
        <linearGradient id="frontBase" x1="0" y1="0" x2="1" y2="0">
          <stop offset="0" stop-color="#45b9ec"/><stop offset=".45" stop-color="#c6e6f5"/><stop offset=".55" stop-color="#f2f4f5"/><stop offset="1" stop-color="#ebecee"/>
        </linearGradient>
        <linearGradient id="deepBlue" x1="0" y1="0" x2="1" y2="0">
          <stop offset="0" stop-color="var(--navy)"/><stop offset="1" stop-color="var(--blue)"/>
        </linearGradient>
        <linearGradient id="skyStep" x1="0" y1="0" x2="1" y2="0">
          <stop offset="0" stop-color="#1f8fe0"/><stop offset=".4" stop-color="#7fd3f5"/><stop offset="1" stop-color="#1a9ce0"/>
        </linearGradient>
      </defs>
      <rect role="img" aria-label="Soft blue photo of a woman in sportswear" width="695" height="490" fill="url(#frontBase)"/>
      <polygon points="270,0 695,0 695,8 490,42 455,60 262,2" fill="url(#deepBlue)"/>
      <g fill="#b9c9e4" opacity=".85">
        <polygon points="520,30 555,8 560,18 528,38"/>
        <polygon points="560,35 595,8 605,18 572,44"/>
        <polygon points="600,42 640,8 652,18 614,52"/>
        <polygon points="640,52 680,14 695,22 656,62"/>
      </g>
      <polyline points="255,0 460,68 505,34 695,102" fill="none" stroke="var(--orange)" stroke-width="2"/>
      <polygon points="0,196 695,360 695,376 0,216" fill="var(--orange)"/>
      <polygon points="0,216 695,376 695,490 0,490" fill="url(#deepBlue)"/>
      <polygon points="521,308 695,350 695,362 517,318" fill="var(--green)"/>
      <polygon points="437,372 493,344 695,404 695,420 496,362 455,382" fill="url(#skyStep)"/>
      <line x1="347" y1="0" x2="347" y2="490" stroke="#c9d3df" stroke-width=".6" opacity=".7"/>
      <circle cx="62" cy="420" r="70" fill="#8a86c6" opacity=".55"/>
    </svg>
    <div style="position:absolute;left:388px;top:140px;transform:rotate(12deg);transform-origin:0 0">
      <div class="brand" style="left:0;top:0;font-size:44px;position:relative"><span class="brand-dot"></span><span class="brand-name">vantrime</span></div>
      <div class="brand-tag" style="left:60px;top:50px;font-size:10px;color:#3a4a66;letter-spacing:.22em">HOME | OFFICE | LIFE</div>
    </div>
    <div class="txt tagline" style="left:151px;top:458px;font-size:16px">HOME | OFFICE | LIFE</div>
    <div class="txt url" style="left:477px;top:459px;font-size:13.5px">www.vantrime.example</div>
  </section>

  <section class="piece letterhead" aria-label="Letterhead">
    <svg viewBox="0 0 296 408" preserveAspectRatio="none">
      <rect x="7" y="0" width="7" height="205" fill="var(--navy)"/>
      <rect x="7" y="205" width="7" height="203" fill="var(--orange)"/>
      <line x1="24" y1="60" x2="284" y2="60" stroke="var(--orange)" stroke-width=".8"/>
      <circle cx="155" cy="255" r="78" fill="#dfe4ee" opacity=".6"/>
      <g fill="#c9d6ea" opacity=".8">
        <polygon points="60,408 85,375 95,375 72,408"/>
        <polygon points="85,408 110,372 122,372 98,408"/>
        <polygon points="110,408 136,368 150,368 126,408"/>
        <polygon points="138,408 164,366 180,366 156,408"/>
      </g>
      <polygon points="170,408 180,395 200,375 230,370 296,362 296,408" fill="var(--navy)"/>
      <polyline points="30,365 170,362 186,348 296,332" fill="none" stroke="var(--orange)" stroke-width="1.2"/>
    </svg>
    <div class="brand" style="left:98px;top:24px;font-size:20px"><span class="brand-dot"></span><span class="brand-name">vantrime</span></div>
    <div class="brand-tag" style="left:132px;top:46px;font-size:4px">HOME | OFFICE | LIFE</div>
    <div class="txt" style="left:32px;top:64px;font-size:6.2px;display:flex;gap:10px">
      <span class="contact">+1 555 0142 318</span>
      <span class="contact">manager@vantrime.example</span>
      <span class="contact">Physical, Address, Here</span>
    </div>
    <div class="txt url" style="right:10px;top:390px;font-size:8px">www.vantrime.example</div>
  </section>

  <section class="piece envelope-back" aria-label="Envelope, back">
    <svg viewBox="0 0 416 214" preserveAspectRatio="none">
      <defs>
        <linearGradient id="envBlue" x1="0" y1="0" x2="1" y2="0">
          <stop offset="0" stop-color="var(--navy)"/><stop offset="1" stop-color="var(--blue)"/>
        </linearGradient>
      </defs>
      <rect width="416" height="214" fill="url(#envBlue)"/>
      <line x1="15" y1="45" x2="400" y2="45" stroke="#fff" stroke-width=".8"/>
      <circle cx="370" cy="175" r="70" fill="#7a8ec0" opacity=".6"/>
    </svg>
    <div class="txt tagline" style="left:0;width:416px;text-align:center;top:27px;font-size:13px">HOME | OFFICE | LIFE</div>
  </section>

  <section class="piece envelope-front" aria-label="Envelope, front">
    <svg viewBox="0 0 425 214" preserveAspectRatio="none">
      <polygon points="0,0 425,0 408,46 15,46" fill="var(--green)"/>
      <g fill="#c9d6ea" opacity=".85">
        <polygon points="150,214 175,172 186,172 162,214"/>
        <polygon points="175,214 200,170 213,170 188,214"/>
        <polygon points="202,214 228,167 242,167 216,214"/>
        <polygon points="230,214 256,165 272,165 246,214"/>
      </g>
      <polygon points="262,214 285,180 300,160 345,162 425,172 425,214" fill="var(--navy)"/>
      <polyline points="95,160 355,168 372,148 425,153" fill="none" stroke="var(--orange)" stroke-width="1.5"/>
    </svg>
    <div class="brand" style="left:20px;top:117px;font-size:20px"><span class="brand-dot"></span><span class="brand-name">vantrime</span></div>
    <div class="brand-tag" style="left:54px;top:139px;font-size:4px">HOME | OFFICE | LIFE</div>
    <div class="txt" style="left:20px;top:160px;font-size:6.2px;line-height:2.05">
      <div class="contact">+1 555 0142 318</div>
      <div class="contact">manager@vantrime.example</div>
      <div class="contact">Physical, Address, Here</div>
    </div>
    <div class="txt url" style="right:14px;top:188px;font-size:9.5px">www.vantrime.example</div>
  </section>

  <section class="piece card card-front" aria-label="Business card, front">
    <svg viewBox="0 0 174 104" preserveAspectRatio="none">
      <polygon points="0,0 174,0 174,3 95,10 82,22 0,10" fill="var(--navy)"/>
      <g fill="#c9d6ea" opacity=".85"><polygon points="120,10 130,3 138,3 128,12"/><polygon points="135,9 146,2 154,2 144,10"/></g>
      <polyline points="0,12 84,24 98,13 174,8" fill="none" stroke="var(--orange)" stroke-width="1"/>
      <polygon points="0,92 174,98 174,104 0,104" fill="var(--navy)"/>
      <polygon points="120,96 174,90 174,98" fill="var(--orange)"/>
    </svg>
    <div class="brand" style="left:34px;top:38px;font-size:17px"><span class="brand-dot"></span><span class="brand-name">vantrime</span></div>
    <div class="brand-tag" style="left:66px;top:58px;font-size:3.6px">HOME | OFFICE | LIFE</div>
  </section>

  <section class="piece card card-back" aria-label="Business card, back">
    <svg viewBox="0 0 174 104" preserveAspectRatio="none">
      <polygon points="0,0 174,0 174,8 0,10" fill="var(--orange)"/>
      <polygon points="60,0 174,0 174,5 90,6" fill="var(--navy)"/>
      <g fill="#c9d6ea" opacity=".85"><polygon points="70,104 80,92 86,92 76,104"/><polygon points="82,104 92,90 99,90 89,104"/></g>
      <polygon points="96,104 108,86 130,84 174,88 174,104" fill="var(--navy)"/>
      <polyline points="20,88 108,86 122,78 174,80" fill="none" stroke="var(--orange)" stroke-width="1"/>
      <circle cx="42" cy="50" r="19" fill="var(--orange)"/>
    </svg>
    <div class="txt" style="left:91px;top:26px;font-family:'Raleway',sans-serif;color:var(--ink);font-size:8px;font-weight:600">ALEX <span style="font-weight:400">MARLOW</span></div>
    <div class="txt" style="left:91px;top:37px;font-size:4.6px;color:var(--orange)">Managing Director</div>
    <div class="txt" style="left:91px;top:45px;font-size:4.2px;line-height:2;color:var(--ink);font-weight:600">
      <div>+1 555 0142 318</div>
      <div>manager@vantrime.example</div>
      <div>Physical, Address, Here</div>
    </div>
  </section>

</main>
</body>
</html>
```